Medical Practice and Business Coaching Website Design

I need a professional website designed for a medical business, DWT Medical.
The website will be hosted on Lumivo (similar design functionality as ZEP).

About the website:
Pages for the website:
- Home page (a brief overview of the company with a section for "Ultrasound Clinics" and "Coaching and Courses" that link to these pages with all the info and packages for these sections)
- About Us (section for company info and info about Marissa Delacourt, founder and business coach)
- Ultrasound Clinics (all the info about ultrasound, our packages, links to book, gallery of 3D/4D images, FAQs, social media links)
- Coaching and Courses (All of our coaching package info, course info with a waiting list sign up, section for free business download resources, social media links, blog posts)
- Contact Us (info for our tarrowby ultrasound location and bookings with a map, contact form, email and phone details)

Pages that are also needed but not visible in the top menu:
- Blog Page
- Waiting List Page x2 (Dubbo pop-up 3D clinic, Online Course)
- Thanks for subscribing page

We have a company logo and a logo for both the ultrasound clinics and the Coaching sides of the business. They are attached as well as the HEX codes for the branding colours. Ideally the company areas of the site will be in the blue, purple and teal colours. The ultrasound clinics page will be mostly in the purple with the "clinics" logo featuring on the page.
The courses and coaching page will be dominant in the blue branding colours with accents of purple and teal. The courses logo will be somewhere on the page too.

About our company:
Our company has 2 separate businesses which will have their own pages on the website.
We have a medical imaging business which specialises in ultrasound. We have 3 locations/services:
- Tarrowby Ultrasound: open Fridays and the occasional saturday. Our main focus and where the focus on the clinical page needs to be.
- East Corrindale Ultrasound: Currently closed, no re-opening date and unlikely to reopen.
- Pop-up clinics: most commonly occur in Dubbo. occasionally in Parkes. Dates for next pop-up will be announced in the future.

Our Blayney practice offers both diagnostic ultrasound (referral from doctor) for all areas of the body and 3d/4d pregnancy ultrasounds for entertainment purposes.
The content for the ultrasound clinics part of the website can be found on the current tarrowby ultrasound website: tarrowbyscans-example.com.au
This website will be replaced by the new company site. All of the info on this site will end up on the clinics page of the new company website.

The second part of the company is a coaching and courses service for medical professionals who want to start or grow their business.
We currently have coaching packages for 1-on-1 online advice and guidance.

Coaching: all take place on Vidlo and can be recorded for them to watch again after. Notes, documents and links that are discussed are provided after session

- FREE 15 minute session: discuss current business or business idea, if and how I can help and potential things they can do. One per client

- Single Coaching Session - 1hr with Marissa

- Silver coaching package: 1 x 1hr Coaching Call with Marissa
Unlimited Email with Marissa for 1 month
Access to our Private Chatterly Group to network with other medical professionals and business owners

- Silver Coaching Package With Social Media Management:
As above with 1 month Social Media Management (15 posts, Chatterly and Snapora)

- Gold coaching package: 2 x 1hr Coaching Calls with Marissa
Access to our Private Chatterly

- Gold Coaching Package With Social Media Management:

- Business Buddy Package: Unlimited Coaching Calls
Unlimited SMS
Unlimited Emails
Social Media Management (Chatterly and Snapora, 1 post per day) Valued at over $700
Business Masterclass (something different each month...social media, medicare, website, branding, live events, etc)

Enrollment for our first course opens in May and clients can join the waitlist in the meantime.
Course is aimed at medical professionals who want to grow their patient numbers and create an online presence for their business.
Ideal for: small practices where the owner does everything, not necessarily familiar with marketing/social media/websites, goes to the very basics and steps through everything in getting a logo, branding, website, building social media pages, creating content.

Course name to come but it will be something like "helpful marketing in healthcare" or "the business of healthcare"

We will also have a blog on the website and a podcast (in the future).

I would like a testimonial on at least the clinics page and the coaching page. Here is one for each but I have more if need be:
Coaching: "I knew I wanted to start my own business but I had no idea where to begin. It would have been easy to abort my dreams of starting my own business had it not been for the direction and unwavering support of Marissa from DWT medical. Marissa dissected the process into manageable bit sized pieces for me and worked tirelessly behind the scenes ensuring everything was on track. Her friendly, warm and approachable manner
equated to more than her just being my business coach, she has now become a friend.
Thank you!!"

Ultrasound testimonial: "Amazing service! Best ultrasound experience I’ve had. Super friendly and informative staff. Great technology. If I didn’t live so far away I’d go to Blayney for all my ultrasounds!"

I would also like a section for a welcome video (yet to be recorded) on the home page, ultrasound clinics page and coaching/courses page.

I've attached the company logo and the sub-logos in different formats. There is also a head shot of Marissa for the about us page, an image of Marissa with a coaching client for the coaching page and multiple 3D ultrasound images for the gallery on the clinics page.

Target Market(s)

Mostly targeted at medical professionals. Pregnant women and anyone needing an ultrasound are the targets for the clinics page

Industry/Entity Type

Healthcare

Number of Pages Required

5+ page

Colors
0054AA
0677BA
7BADD7
CADEEF
E8F1F8
0094D4
00A9DD
6FCCEA
C7EBF8
E9F6FB
00AB8E
00BBA5
67D7C9
C6EFE9
E9F9F6
A7469A
B969AE
D3A5CF
EDDBEB
F8F0F9
6B429C
8869AF
B7A5CE
E3DAEB
F3F0F8

```html
<!DOCTYPE html>
<html lang="en">
<head>
<meta charset="utf-8">
<title>DWT Medical</title>
<link href="https://fonts.googleapis.com/css2?family=Tinos:wght@400;700&family=Poppins:wght@400&display=swap" rel="stylesheet">
<style>
:root{
  --purple:#5b2f92;
  --purple-soft:#6B429C;
  --purple-pale:#E3DAEB;
  --blue:#0677BA;
  --ink:#1c1c1c;
  --body:#3a3a3a;
  --band:#d6e6f3;
  --line:#d9d9d9;
  --white:#ffffff;
}
*{box-sizing:border-box;margin:0;padding:0}
html,body{width:1200px;height:3266px;overflow:hidden;background:var(--white)}
body{position:relative;font-family:'Poppins',sans-serif;color:var(--body)}
.abs{position:absolute}
.btn{position:absolute;display:flex;align-items:center;justify-content:center;background:var(--blue);color:var(--white);border-radius:34px;font-family:'Tinos',serif;font-weight:700;letter-spacing:1.5px;font-size:16px;text-transform:uppercase}
.photo{position:absolute}

/* brand marks: plain circle + name */
.brand-mark{width:70px;height:70px;border-radius:50%;background:var(--purple-pale)}
.brand-name{font-family:'Tinos',serif;font-weight:400;color:var(--purple-soft);font-size:22px;white-space:nowrap;margin-top:14px}

/* header */
.site-header{position:absolute;left:0;top:0;width:1200px;height:127px;background:var(--white)}
.brand-block{position:absolute;left:75px;top:0;width:151px;height:209px;background:var(--white);z-index:3;display:flex;flex-direction:column;align-items:center;padding-top:40px}
.header-phone{left:686px;top:24px;font-family:'Tinos',serif;font-weight:700;font-size:21px;color:var(--ink);display:flex;align-items:center;gap:10px}
.main-nav{position:absolute;left:305px;top:86px;display:flex;gap:44px;font-family:'Tinos',serif;font-size:14px;letter-spacing:1px;color:var(--ink)}
.main-nav .active{color:var(--purple-soft)}

/* hero */
.hero{position:absolute;left:0;top:127px;width:1200px;height:674px;background:linear-gradient(110deg,#8a8d92 0%,#c9c6c4 30%,#6e7178 52%,#d8d2cd 75%,#a8a39e 100%)}
.hero-shade{position:absolute;inset:0;background:rgba(20,20,30,.28)}
.hero-title{position:absolute;left:0;width:1200px;top:212px;text-align:center;font-family:'Tinos',serif;font-weight:700;font-size:78px;color:var(--white);letter-spacing:2px}
.hero-sub{position:absolute;left:0;width:1200px;top:300px;text-align:center;color:var(--white);font-size:24px;line-height:34px}

/* sections */
.h2{position:absolute;font-family:'Tinos',serif;font-weight:400;font-size:42px;letter-spacing:3px;color:var(--ink);text-transform:uppercase;white-space:nowrap}
.h2 em{font-style:normal;color:var(--purple)}
.copy{position:absolute;font-size:15.5px;line-height:34px;color:var(--body)}
.welcome-mark{position:absolute;left:109px;top:890px;width:260px;display:flex;flex-direction:column;align-items:center}
.welcome-mark .brand-mark{width:260px;height:260px}
.welcome-mark .brand-name{font-size:28px;margin-top:20px}
.caption{position:absolute;text-align:center;font-family:'Tinos',serif;font-weight:700;font-size:22px;line-height:27px;color:var(--purple-soft);letter-spacing:1px}
.play{position:absolute;left:388px;top:1506px}

/* blog */
.blog-band{position:absolute;left:0;top:2276px;width:1200px;height:592px;background:var(--band)}
.post{position:absolute;top:2409px;width:242px}
.post-img{height:173px}
.post-title{font-family:'Tinos',serif;font-weight:700;font-size:23px;line-height:27px;color:var(--purple-soft);margin-top:22px;width:215px}
.post-text{font-size:15px;line-height:26px;color:var(--body);margin-top:6px}
.view-all{position:absolute;left:0;width:1200px;top:2784px;text-align:center;font-family:'Tinos',serif;font-size:18px;color:var(--blue);text-decoration:underline;letter-spacing:.5px}

/* footer */
.foot-brand{position:absolute;left:75px;top:2945px;width:128px;display:flex;flex-direction:column;align-items:center}
.foot-brand .brand-mark{width:100px;height:100px}
.foot-col{position:absolute;top:2933px;font-family:'Tinos',serif;font-size:15px;color:var(--ink);letter-spacing:.4px}
.foot-col h4{font-size:18px;color:var(--purple-soft);font-weight:700;letter-spacing:1px;margin-bottom:10px}
.foot-col li{list-style:none;line-height:33px}
.foot-col .link{color:var(--blue)}
.rule{position:absolute;left:0;top:3198px;width:1200px;height:1px;background:var(--line)}
.copyright{position:absolute;left:75px;top:3222px;font-size:14px;color:var(--body)}
.social{position:absolute;right:75px;top:3222px;display:flex;gap:16px;font-family:'Tinos',serif;font-size:14px;color:var(--blue)}
</style>
</head>
<body>

<header class="site-header">
  <div class="brand-block">
    <div class="brand-mark"></div>
    <div class="brand-name">DWT Medical</div>
  </div>
  <div class="abs header-phone">
    <svg width="18" height="20" viewBox="0 0 24 24"><path d="M6.6 10.8a15.1 15.1 0 0 0 6.6 6.6l2.2-2.2a1 1 0 0 1 1-.25 11.4 11.4 0 0 0 3.6.57 1 1 0 0 1 1 1V20a1 1 0 0 1-1 1A17 17 0 0 1 3 4a1 1 0 0 1 1-1h3.5a1 1 0 0 1 1 1c0 1.25.2 2.45.57 3.6a1 1 0 0 1-.25 1z" fill="#5b2f92"/></svg>
    +1-800-555-0142
  </div>
  <div class="btn" style="left:904px;top:14px;width:222px;height:52px;font-size:13px;letter-spacing:1px">Book an appointment</div>
  <nav class="main-nav">
    <span class="active">HOME</span><span>ABOUT US</span><span>COACHING &amp; COURSES</span><span>ULTRASOUND CLINICS</span><span>BLOG</span><span>CONTACT US</span>
  </nav>
</header>

<section class="hero" role="img" aria-label="Sonographer performing a pregnancy ultrasound on a smiling patient, monitor showing a scan">
  <div class="hero-shade"></div>
  <h1 class="hero-title">DWT MEDICAL</h1>
  <p class="hero-sub">Sed ut perspiciatis unde omnis iste natus error sit voluptatem<br>accusantium doloremque laudantium.</p>
  <div class="btn" style="left:456px;top:380px;width:287px;height:66px">Book an appointment</div>
</section>

<section class="welcome">
  <div class="welcome-mark"><div class="brand-mark"></div><div class="brand-name">DWT Medical</div></div>
  <h2 class="h2" style="left:435px;top:880px">Welcome to <em>DWT Medical</em></h2>
  <p class="copy" style="left:434px;top:950px;width:690px;font-size:16px">Sed ut perspiciatis unde omnis iste natus error sit voluptatem accusantium doloremque laudantium, totam rem aperiam, eaque ipsa quae ab illo inventore veritatis et quasi architecto beatae vitae dicta sunt explicabo. Nemo enim ipsam voluptatem quia voluptas sit aspernatur aut odit aut fugit, sed quia consequuntur magni dolores eos qui ratione voluptatem sequi nesciunt.</p>
  <div class="btn" style="left:434px;top:1159px;width:213px;height:66px">Read more</div>
</section>

<section class="about">
  <div class="photo" style="left:75px;top:1333px;width:691px;height:409px;background:linear-gradient(100deg,#b8a8a6 0%,#c85d55 22%,#d6d0c8 45%,#9c9a98 70%,#cfcfd2 100%)" role="img" aria-label="Welcome video: two women smiling beside an ultrasound machine"></div>
  <svg class="play" width="66" height="66" viewBox="0 0 66 66"><circle cx="33" cy="33" r="30" fill="none" stroke="#fff" stroke-width="5"/><path d="M26 19 L48 33 L26 47 Z" fill="#fff"/></svg>
  <h2 class="h2" style="left:795px;top:1370px">About us</h2>
  <p class="copy" style="left:794px;top:1436px;width:330px;line-height:33px">Sed ut perspiciatis unde omnis iste natus error sit voluptatem accusantium doloremque laudantium, totam rem aperiam, eaque ipsa quae ab illo in ventore veritatis et quasi.</p>
  <div class="btn" style="left:794px;top:1627px;width:213px;height:67px">Read more</div>
</section>

<section class="services">
  <h2 class="h2" style="left:79px;top:1845px">What we do</h2>
  <p class="copy" style="left:75px;top:1910px;width:330px;line-height:33px">Sed ut perspiciatis unde omnis iste natus error sit voluptatem accusantium doloremque laudantium, totam rem aperiam, eaque ipsa quae ab illo in ventore veritatis et quasi.</p>
  <div class="btn" style="left:75px;top:2102px;width:213px;height:66px">Read more</div>
  <div class="photo" style="left:436px;top:1841px;width:329px;height:279px;background:linear-gradient(160deg,#1b2230 0%,#3b5775 45%,#cfd5dc 100%)" role="img" aria-label="Gloved hand pointing at an ultrasound scan on a monitor"></div>
  <div class="caption" style="left:436px;top:2136px;width:329px">ULTRASOUND<br>CLINICS</div>
  <div class="photo" style="left:796px;top:1841px;width:330px;height:279px;background:linear-gradient(150deg,#e9e6e3 0%,#c7b3a6 40%,#6d7b8c 75%,#e5e7ea 100%)" role="img" aria-label="Group of medical professionals gathered around a laptop"></div>
  <div class="caption" style="left:796px;top:2136px;width:330px">COACHING &amp;<br>COURSES</div>
</section>

<section class="blog-band">
  <h2 class="h2" style="left:0;width:1200px;text-align:center;top:52px">Blog posts</h2>
</section>
<article class="post" style="left:75px"><div class="post-img" style="background:linear-gradient(135deg,#111 0%,#9c7a52 45%,#e6cba1 70%,#2a1d10 100%)" role="img" aria-label="3D ultrasound image of a baby"></div><h3 class="post-title">Sed ut perspiciatis unde omnis</h3><p class="post-text">Natus error sit voluptatem accusantium doloremque laudantium.</p></article>
<article class="post" style="left:345px"><div class="post-img" style="background:linear-gradient(120deg,#8e9196 0%,#d4cfca 45%,#6a6e76 70%,#d7d1cb 100%)" role="img" aria-label="Sonographer scanning a pregnant patient"></div><h3 class="post-title">Sed ut perspiciatis unde omnis</h3><p class="post-text">Natus error sit voluptatem accusantium doloremque laudantium.</p></article>
<article class="post" style="left:614px"><div class="post-img" style="background:linear-gradient(150deg,#d8dde6 0%,#9fb3d0 40%,#e9e3de 70%,#b6a9a0 100%)" role="img" aria-label="Ultrasound probe on a patient's abdomen"></div><h3 class="post-title">Sed ut perspiciatis unde omnis</h3><p class="post-text">Natus error sit voluptatem accusantium doloremque laudantium.</p></article>
<article class="post" style="left:884px"><div class="post-img" style="background:linear-gradient(120deg,#cfd6df 0%,#eef0f3 40%,#8fa6c8 70%,#e3e6ea 100%)" role="img" aria-label="Medical team attending to a patient in a ward"></div><h3 class="post-title">Sed ut perspiciatis unde omnis</h3><p class="post-text">Natus error sit voluptatem accusantium doloremque laudantium.</p></article>
<a class="view-all">View All Blog Posts</a>

<footer>
  <div class="foot-brand"><div class="brand-mark"></div><div class="brand-name">DWT Medical</div></div>
  <div class="foot-col" style="left:311px"><h4>SITE MAP</h4><ul><li>Home</li><li>About Us</li><li>Coaching &amp; Courses</li><li>Ultrasound Clinics</li><li>Blog</li><li>Contact Us</li></ul></div>
  <div class="foot-col" style="left:581px"><h4>SERVICES</h4><ul><li>Sed ut perspiciatis</li><li>Unde omnis iste</li><li>Natus error sit</li><li>Voluptatem accusantium</li><li>Laudantium</li></ul></div>
  <div class="foot-col" style="left:886px"><h4>CONTACT US</h4><ul><li style="line-height:28px;margin:3px 0 6px">Sed ut perspiciatis unde<br>omnis iste natus</li><li style="line-height:30px">1-800-555-0142</li><li style="line-height:30px">info@dwtmedical-example.com</li><li class="link">Map Locations</li></ul></div>
  <div class="rule"></div>
  <p class="copyright">Copyright © 2022. CompanyName.&nbsp; All Right Reserved</p>
  <div class="social"><span>Chatterly</span><span>Chirply</span><span>Streamly</span><span>Snapora</span></div>
</footer>

</body>
</html>
```